Bref créative |
Tern Ledger | ||
Business Cards and Letterheads | ||
Use standard fonts | ||
Cutting-Edge Professional Simple |
Ronald Pyke | ||
Suite 412, Level 4, 35 Gorse St, Sydney, NSW, 2000 | ||
ronald@ternledger-example.com | ||
www.ternledger-example.com | ||
Good Luck! | ||
<< Up to the designer >> | ||

```html
<!DOCTYPE html>
<html lang="en">
<head>
<meta charset="utf-8">
<title>Tern Ledger – Business Cards</title>
<link href="https://fonts.googleapis.com/css2?family=Montserrat:wght@400;500;700;800&display=swap" rel="stylesheet">
<style>
  :root {
    --backdrop: #e9e6e1;
    --ink: #161616;
    --panel-black: #1c1c1c;
    --steel-light: #f2f2f2;
    --steel-mid: #d6d6d6;
    --steel-dark: #b9b9b9;
    --text-grey: #4a4a4a;
    --accent: #f39323;
  }
  * { margin: 0; padding: 0; box-sizing: border-box; }
  html, body {
    width: 1200px; height: 886px; overflow: hidden;
    background: var(--backdrop);
    font-family: "Montserrat", Arial, sans-serif;
  }
  .sheet { position: relative; width: 1200px; height: 886px; }

  .card {
    position: absolute;
    width: 620px; height: 378px;
    overflow: hidden;
    background:
      repeating-linear-gradient(100deg, rgba(255,255,255,0.18) 0 1px, rgba(0,0,0,0.03) 1px 3px),
      linear-gradient(125deg, var(--steel-dark) 0%, var(--steel-light) 40%, var(--steel-mid) 65%, var(--steel-light) 100%);
    box-shadow: 0 10px 24px rgba(0,0,0,0.22);
  }
  .card--front { left: 90px; top: 60px; }
  .card--back { left: 490px; top: 448px; }

  .card__panels { position: absolute; inset: 0; width: 100%; height: 100%; }
  .card__panels polygon { fill: var(--panel-black); }

  .brand {
    position: absolute;
    display: flex; align-items: center; gap: 12px;
    font-weight: 800;
    letter-spacing: -0.5px;
    color: var(--ink);
    text-transform: uppercase;
    white-space: nowrap;
  }
  .brand__dot {
    width: 26px; height: 26px; border-radius: 50%;
    background: var(--accent);
    flex: none;
  }
  .card--front .brand { left: 130px; top: 188px; font-size: 40px; }
  .card--back .brand { left: 50%; top: 190px; transform: translateX(-50%); font-size: 36px; }

  .holder {
    position: absolute; right: 26px; top: 22px; text-align: right;
    color: var(--text-grey);
  }
  .holder__name { font-size: 27px; font-weight: 500; color: #333; }
  .holder__email { font-size: 14px; margin-top: 4px; }

  .contact {
    position: absolute; left: 26px; bottom: 24px;
    display: flex; gap: 26px;
    font-size: 13px; line-height: 1.55; color: var(--text-grey);
  }
  .contact__phones { display: grid; grid-template-columns: auto auto; column-gap: 14px; }

  .web {
    position: absolute; left: 0; right: 0; top: 246px;
    text-align: center; font-size: 14px; color: var(--text-grey);
  }
</style>
</head>
<body>
<main class="sheet">
  <section class="card card--front" aria-label="Business card front">
    <svg class="card__panels" viewBox="0 0 100 61" preserveAspectRatio="none" aria-hidden="true">
      <polygon points="0,0 39,0 0,30"/>
      <polygon points="100,21 100,61 60,61"/>
    </svg>
    <div class="holder">
      <p class="holder__name">Ronald Pyke</p>
      <p class="holder__email">ronald@ternledger-example.com</p>
    </div>
    <div class="brand"><span class="brand__dot"></span>Tern Ledger</div>
    <div class="contact">
      <address class="contact__address" style="font-style:normal">
        Suite 412, Level 4,<br>35 Gorse St, Sydney,<br>NSW, 2000
      </address>
      <div class="contact__phones">
        <span>Ph:</span><span>+61 2 9000 4120</span>
        <span>Cell:</span><span>+61 400 555 218</span>
        <span>Fax:</span><span>+61 2 9000 4121</span>
      </div>
    </div>
  </section>

  <section class="card card--back" aria-label="Business card back">
    <svg class="card__panels" viewBox="0 0 100 61" preserveAspectRatio="none" aria-hidden="true">
      <polygon points="0,0 37,0 0,48"/>
      <polygon points="100,7 100,61 67,61"/>
    </svg>
    <div class="brand"><span class="brand__dot"></span>Tern Ledger</div>
    <p class="web">www.ternledger-example.com</p>
  </section>
</main>
</body>
</html>
```